I need an amazing business card!

I am the principle in my own software company that develops zelPad and mobile applications. I require a great business card design. I've attached my corporate logo (Thanks Teodor!).
I would like the design to integrate the logo, my name, email address and skype account:
name Brent Halvorsen
email brenthalvorsen@tvekra.com
skype brenthalvorsen.net
I would like the back of the card to have a "write on me area" similar to the "write on me" card on this page, row 6:
http://us.plinkora.com/design-templates/business-cards/#industry=Computing%20%26%20IT
As far as the rest - it's all you!
Updates
1) Please add an example telephone number as well.
Industry/Entity Type
Software
Look and feel
Each slider illustrates characteristics of the customer's brand and the style your logo design should communicate.

```html
<!DOCTYPE html>
<html lang="en">
<head>
<meta charset="utf-8">
<title>Tvekra business card – front and back</title>
<link rel="stylesheet" href="https://fonts.googleapis.com/css2?family=Open+Sans:wght@300;400&display=swap">
<style>
  :root {
    --canvas-bg: #e4e4e2;
    --card-white: #ffffff;
    --card-green: #a4c43c;
    --green-light: #b4d152;
    --green-mark: #8fb32c;
    --green-faint: #eef3e0;
    --ink-white: #ffffff;
    --rule-grey: #5a5a5a;
    --shadow: rgba(0, 0, 0, 0.18);
  }
  * { box-sizing: border-box; margin: 0; padding: 0; }
  html, body {
    width: 1200px;
    height: 873px;
    overflow: hidden;
    background: var(--canvas-bg);
    font-family: "Open Sans", Arial, sans-serif;
  }
  .canvas {
    width: 1200px;
    height: 873px;
    display: flex;
    align-items: center;
    justify-content: center;
    gap: 40px;
  }
  .card {
    position: relative;
    width: 540px;
    height: 310px;
    border-radius: 3px;
    box-shadow: 0 6px 18px var(--shadow);
    overflow: hidden;
  }

  /* Back: write-on area */
  .card-back { background: var(--card-white); }
  .back-brand {
    position: absolute;
    top: 22px;
    right: 24px;
    display: flex;
    flex-direction: column;
    align-items: flex-end;
    gap: 4px;
  }
  .brand-square {
    width: 34px;
    height: 34px;
    border-radius: 7px;
    background: var(--green-mark);
  }
  .brand-name-small {
    font-weight: 400;
    font-size: 10px;
    letter-spacing: 5px;
    color: var(--green-mark);
  }
  .back-watermark {
    position: absolute;
    left: 50%;
    top: 50%;
    transform: translate(-50%, -50%);
    display: flex;
    align-items: center;
    gap: 20px;
  }
  .watermark-square {
    width: 150px;
    height: 150px;
    border-radius: 28px;
    background: var(--green-faint);
  }
  .watermark-name {
    font-weight: 400;
    font-size: 30px;
    letter-spacing: 16px;
    color: var(--green-faint);
  }
  .write-lines {
    position: absolute;
    left: 40px;
    right: 40px;
    top: 84px;
  }
  .write-line {
    height: 1px;
    background: var(--rule-grey);
    margin-bottom: 34px;
  }

  /* Front: identity */
  .card-front { background: var(--card-green); }
  .front-brand {
    position: absolute;
    top: 30px;
    left: 34px;
    display: flex;
    align-items: flex-end;
    gap: 18px;
  }
  .brand-square-large {
    width: 92px;
    height: 92px;
    border-radius: 18px;
    background: var(--green-light);
  }
  .brand-name-large {
    font-weight: 400;
    font-size: 20px;
    letter-spacing: 14px;
    color: var(--ink-white);
  }
  .holder-name {
    position: absolute;
    right: 40px;
    top: 150px;
    font-weight: 300;
    font-size: 30px;
    color: var(--ink-white);
  }
  .contact-list {
    position: absolute;
    left: 40px;
    bottom: 36px;
    list-style: none;
    font-weight: 300;
    font-size: 14px;
    line-height: 1.6;
    color: var(--ink-white);
  }
</style>
</head>
<body>
<main class="canvas">
  <section class="card card-back" aria-label="Card back with write-on lines">
    <div class="back-watermark" aria-hidden="true">
      <div class="watermark-square"></div>
      <span class="watermark-name">tvekra</span>
    </div>
    <div class="write-lines">
      <div class="write-line"></div>
      <div class="write-line"></div>
      <div class="write-line"></div>
      <div class="write-line"></div>
      <div class="write-line"></div>
    </div>
    <div class="back-brand">
      <div class="brand-square"></div>
      <span class="brand-name-small">tvekra</span>
    </div>
  </section>

  <section class="card card-front" aria-label="Card front with contact details">
    <div class="front-brand">
      <div class="brand-square-large"></div>
      <span class="brand-name-large">tvekra</span>
    </div>
    <h1 class="holder-name">Brent Halvorsen</h1>
    <ul class="contact-list">
      <li>Tel: 123456789</li>
      <li>Email: brenthalvorsen@tvekra.com</li>
      <li>Skype: brenthalvorsen.net</li>
    </ul>
  </section>
</main>
</body>
</html>
```